We need a MODERN credit application banner

We have a program that helps people get pre-qualified for an auto loan. Our current Application page/Success page is dated and does not have the colors we want. I want to use fonts and colors that match our partner CrestLedger (www.crestledger-demo.com). I want to include their powered by logo, tallymark rating logo, and swift4lending logo all in a matching CrestLedger Color scheme. I also need a Favicon that matches your design for the page. I attached our deck so you can get more content. To be clear the application page and success pages below are the targets of this redesign! You can visit www.pbelvoiradvertising-demo.com to get more information from our website or www.swift4lending-demo.com.

Target Market(s)

Car dealers and their consumers

Industry/Entity Type

Automotive

Requirements
Must have
• It must offer the same data that is on the existing art
Nice to have
• Looking for a Clean but Interesting design.
Should not have
• No red and black. Do not change the form fills.

```html
<!DOCTYPE html>
<html lang="en">
<head>
<meta charset="utf-8">
<title>Swift4Lending – Credit Pre-Qualification</title>
<link rel="stylesheet" href="https://fonts.googleapis.com/css2?family=Roboto:wght@400;500;700;900&display=swap">
<style>
  :root{
    --canvas:#ededed;
    --white:#ffffff;
    --brand:#1a9fc4;
    --teal-panel:rgba(27,98,118,0.86);
    --teal-dark:#0c5468;
    --teal-deep:#0f4a5c;
    --yellow:#f9d700;
    --yellow-text:#f6d22a;
    --bar:#dfe7ea;
    --bar-text:#2e3b42;
    --icon-grey:#9a9a9a;
  }
  *{box-sizing:border-box;margin:0;padding:0}
  html,body{width:1200px;height:2178px;overflow:hidden}
  body{background:var(--canvas);font-family:"Roboto",Arial,sans-serif;position:relative;color:var(--white)}

  .page{position:absolute;left:74px;width:1051px;background:var(--white);box-shadow:0 2px 10px rgba(0,0,0,.18)}
  .page--apply{top:57px;height:1003px}
  .page--success{top:1114px;height:1011px}

  .site-header{height:105px;position:relative;background:var(--white)}
  .brand-name{position:absolute;left:22px;top:36px;font-size:29px;font-weight:700;color:var(--brand);letter-spacing:-.3px;text-transform:uppercase}
  .social{position:absolute;right:24px;top:35px;display:flex;gap:5px}
  .social span{width:32px;height:32px;border:1.5px solid var(--icon-grey);border-radius:50%;display:block}

  .hero{position:relative;overflow:hidden}
  .page--apply .hero{height:836px;background:linear-gradient(100deg,#b9c3c8 0%,#aebbc2 40%,#8c8781 62%,#9c8f86 78%,#c9c4bf 100%)}
  .page--success .hero{height:844px;background:linear-gradient(160deg,#9eb0b8 0%,#6f8c98 35%,#5d7f8c 60%,#b7a596 85%,#d7cfc7 100%)}
  .hero-photo{position:absolute;inset:0}

  .site-footer{height:62px;background:var(--teal-dark);position:relative}
  .powered{position:absolute;left:53px;top:10px}
  .powered small{display:block;font-size:11px;color:#c9d7dc}
  .powered strong{font-size:27px;font-weight:400;color:var(--brand);line-height:28px}
  .partner{position:absolute;left:246px;top:24px;font-size:15px;font-weight:400;color:var(--brand);display:flex;align-items:center;gap:6px}
  .partner i{width:22px;height:22px;background:var(--brand);display:block}
  .copyright{position:absolute;right:53px;top:23px;font-size:15px;color:var(--white)}
  .code{position:absolute;right:17px;top:40px;font-size:14px;color:var(--white)}

  /* Application form */
  .form-panel{position:absolute;left:55px;top:44px;width:612px;height:736px;background:var(--teal-panel);border:3px solid var(--yellow);border-radius:32px;padding:0 32px}
  .form-title{margin-top:36px;text-align:center;font-size:29px;font-weight:700;letter-spacing:.3px}
  .form-sub{margin-top:12px;text-align:center;font-size:18px;font-weight:700;color:var(--yellow-text)}
  .divider{height:1px;margin:20px 30px 0;background:linear-gradient(90deg,transparent,var(--yellow),transparent)}
  .fields{margin-top:14px;display:grid;grid-template-columns:263px 263px;column-gap:23px;row-gap:15px}
  .field label{display:block;font-size:13.5px;margin-bottom:5px}
  .input{height:36px;border:1px solid rgba(255,255,255,.9);border-radius:3px;position:relative;font-size:13px;display:flex;align-items:center;padding-left:9px;color:#e8f1f4}
  .field--wide{grid-column:1 / 3}
  .field--wide .input{width:547px}
  .select::after{content:"";position:absolute;right:12px;top:15px;border:4px solid transparent;border-top:5px solid var(--white)}
  .dob{display:flex;gap:9px}
  .dob .input{width:82px}
  .btn-submit{position:absolute;left:163px;top:648px;width:282px;height:52px;border-radius:26px;background:var(--yellow);color:var(--teal-deep);font-size:16px;font-weight:500;display:flex;align-items:center;justify-content:center}

  /* Success panel */
  .result-panel{position:absolute;left:36px;top:47px;width:977px;height:749px;background:var(--teal-panel);border:3px solid var(--yellow);border-radius:36px;text-align:center}
  .result-panel h1{position:absolute;left:0;right:0;top:34px;font-size:32px;font-weight:700}
  .result-sub{position:absolute;left:0;right:0;top:84px;font-size:20px;font-weight:700;color:var(--yellow-text)}
  .congrats{position:absolute;left:0;right:0;top:138px;font-size:45px;font-weight:400}
  .qualify{position:absolute;left:0;right:0;top:198px;font-size:28px;font-weight:700;color:var(--yellow-text)}
  .next-step{position:absolute;left:0;right:0;top:258px;font-size:46px;font-weight:700}
  .step{position:absolute;top:346px;width:220px;margin-left:-110px}
  .step .circle{width:115px;height:115px;margin:0 auto;border:3px solid var(--yellow);border-radius:50%;background:rgba(12,70,88,.55);display:flex;align-items:center;justify-content:center}
  .step p{margin-top:21px;font-size:14.5px;font-weight:700;line-height:22px;letter-spacing:.2px}
  .actions{position:absolute;top:556px;left:312px;display:flex;gap:10px}
  .btn{height:48px;width:172px;border-radius:24px;font-size:14px;font-weight:700;display:flex;align-items:center;justify-content:center;color:var(--yellow-text)}
  .btn--solid{background:var(--yellow);color:var(--teal-deep)}
  .btn--ghost{border:2px solid var(--yellow)}
  .validity{position:absolute;left:47px;top:641px;width:883px;height:66px;background:var(--bar);border:1px solid #c9d4d8;display:flex;align-items:center;padding-left:35px;color:var(--bar-text);font-size:21px;font-weight:500}
  .btn-act{position:absolute;right:28px;top:11px;width:143px;height:42px;border-radius:21px;background:var(--teal-dark);color:var(--white);font-size:16px;font-weight:700;display:flex;align-items:center;justify-content:center}

  .badge{position:absolute;left:865px;top:14px;width:165px;height:165px;color:var(--teal-deep);text-align:center}
  .badge svg{position:absolute;inset:0}
  .badge-text{position:absolute;inset:0;display:flex;flex-direction:column;align-items:center;justify-content:center;font-weight:700}
  .badge-text .up{font-size:20px;font-weight:500}
  .badge-text .amt{font-size:30px;line-height:34px}
  .badge-text .lbl{font-size:10.5px;line-height:15px}
</style>
</head>
<body>

<section class="page page--apply">
  <header class="site-header">
    <div class="brand-name">Swift4Lending</div>
    <nav class="social" aria-label="Social links"><span></span><span></span><span></span><span></span><span></span></nav>
  </header>
  <div class="hero">
    <div class="hero-photo" role="img" aria-label="Photo of a woman holding a payment card while using a laptop by a bright window"></div>
    <form class="form-panel">
      <h2 class="form-title">GET YOUR FREE CREDIT SCORE</h2>
      <p class="form-sub">AND GET PRE-QUALIFIED INSTANTLY</p>
      <div class="divider"></div>
      <div class="fields">
        <div class="field"><label>First Name *</label><div class="input"></div></div>
        <div class="field"><label>Last Name *</label><div class="input"></div></div>
        <div class="field"><label>Address*</label><div class="input"></div></div>
        <div class="field"><label>Apartment</label><div class="input"></div></div>
        <div class="field"><label>City*</label><div class="input"></div></div>
        <div class="field"><label>State*</label><div class="input select"></div></div>
        <div class="field"><label>Zip*</label><div class="input"></div></div>
        <div class="field"><label>Date of Birth*</label>
          <div class="dob"><div class="input select">dd</div><div class="input select">mm</div><div class="input select">yyyy</div></div>
        </div>
        <div class="field"><label>Mobile Phone*</label><div class="input"></div></div>
        <div class="field"><label>Email*</label><div class="input"></div></div>
        <div class="field field--wide"><label>The Vehicle L'm most interested in is Category :</label><div class="input select"></div></div>
        <div class="field field--wide"><label>Make</label><div class="input select"></div></div>
      </div>
      <div class="btn-submit">GET RESULTS</div>
    </form>
  </div>
  <footer class="site-footer">
    <div class="powered"><small>Powered by:</small><strong>CrestLedger</strong></div>
    <div class="partner"><i></i>TallyMark Rating</div>
    <div class="copyright">© Copyright 2022.All Rights Reserved</div>
    <div class="code">C2</div>
  </footer>
</section>

<section class="page page--success">
  <header class="site-header">
    <div class="brand-name">Swift4Lending</div>
    <nav class="social" aria-label="Social links"><span></span><span></span><span></span><span></span><span></span></nav>
  </header>
  <div class="hero">
    <div class="hero-photo" role="img" aria-label="Photo of hands holding a payment card over a laptop keyboard"></div>
    <div class="result-panel">
      <h1>SUCCESS</h1>
      <p class="result-sub">VIEW YOUR CREDIT SCORE AND PRE-QUALIFICATION AMOUNT</p>
      <p class="congrats">CONGRATULATIONS!</p>
      <p class="qualify">YOU PRE-QUALIFY FOR UP TO $75,000</p>
      <p class="next-step">YOU CAN TAKE THE NEXT STEP</p>

      <div class="step" style="left:250px">
        <div class="circle">
          <svg width="40" height="40" viewBox="0 0 24 24"><path fill="#f9d700" d="M6.6 10.8a15.1 15.1 0 0 0 6.6 6.6l2.2-2.2a1 1 0 0 1 1-.25 11.4 11.4 0 0 0 3.6.57 1 1 0 0 1 1 1V20a1 1 0 0 1-1 1A17 17 0 0 1 3 4a1 1 0 0 1 1-1h3.5a1 1 0 0 1 1 1c0 1.25.2 2.45.57 3.57a1 1 0 0 1-.25 1z"/></svg>
        </div>
        <p>CALL ABC DEALER AT<br>555-014-2290</p>
      </div>
      <div class="step" style="left:489px">
        <div class="circle">
          <svg width="46" height="42" viewBox="0 0 46 42"><path fill="none" stroke="#f9d700" stroke-width="4" stroke-linejoin="round" d="M3 16 23 3l20 13v22H3z M3 16l20 13 20-13"/></svg>
        </div>
        <p>EMAIL THEM BY<br>CLICKING HERE</p>
      </div>
      <div class="step" style="left:727px">
        <div class="circle">
          <svg width="44" height="40" viewBox="0 0 44 40"><rect x="11" y="2" width="22" height="12" fill="none" stroke="#f9d700" stroke-width="4"/><rect x="2" y="14" width="40" height="16" rx="3" fill="#f9d700"/><rect x="11" y="24" width="22" height="14" fill="#0f4a5c" stroke="#f9d700" stroke-width="4"/></svg>
        </div>
        <p>PRINT THIS PAGE AND<br>TAKE IT TO ABC DEALER</p>
      </div>

      <div class="actions">
        <div class="btn btn--solid">PRINTABLE VERSION</div>
        <div class="btn btn--ghost">MAP TO DEALER</div>
      </div>

      <div class="validity">YOUR PRE-QUALIFICATION IS VALID OR A LIMITED TIME
        <div class="btn-act">ACT NOW!</div>
      </div>
    </div>

    <div class="badge">
      <svg viewBox="0 0 200 200" aria-hidden="true">
        <g fill="#f9d700">
          <rect x="29" y="29" width="142" height="142" transform="rotate(0 100 100)"/>
          <rect x="29" y="29" width="142" height="142" transform="rotate(15 100 100)"/>
          <rect x="29" y="29" width="142" height="142" transform="rotate(30 100 100)"/>
          <rect x="29" y="29" width="142" height="142" transform="rotate(45 100 100)"/>
          <rect x="29" y="29" width="142" height="142" transform="rotate(60 100 100)"/>
          <rect x="29" y="29" width="142" height="142" transform="rotate(75 100 100)"/>
        </g>
      </svg>
      <div class="badge-text">
        <span class="up">UPTO</span>
        <span class="amt">$75,000</span>
        <span class="lbl">PRE-QUALIFICATION<br>AMOUNT</span>
      </div>
    </div>
  </div>
  <footer class="site-footer">
    <div class="powered"><small>Powered by:</small><strong>CrestLedger</strong></div>
    <div class="partner"><i></i>TallyMark Rating</div>
    <div class="copyright">© Copyright 2022.All Rights Reserved</div>
    <div class="code">C2</div>
  </footer>
</section>

</body>
</html>
```